Boutique Real Estate Brokerage looking for business card, letterhead and envelope design

We are looking for a cohesive design for our business cards, letterhead and envelopes and that mirrors our high-end homes and clientele. Fern & Gable is being launched and designed for the marketplace of tomorrow. We grew from the #1 team in our community into a full-service firm that is going to revolutionize the traditional real estate model.

We understand that it’s more important than ever to help our clients and partners adapt to behavioral and market changes being driven by generational shifts and technological advances in society, and by combining traditional brokerage services with innovative production and marketing capabilities, we know how to do that better than anyone else.

Requirements
Must have
• business card, letterhead and envelope design - attached logo.

```html
<!DOCTYPE html>
<html lang="en">
<head>
<meta charset="utf-8">
<title>Fern &amp; Gable Realty — Stationery</title>
<link href="https://fonts.googleapis.com/css2?family=Lato:wght@400;700&family=Montserrat:wght@700&family=Open+Sans:wght@400&display=swap" rel="stylesheet">
<style>
  :root{
    --bg:#e6e6e8;
    --paper:#ffffff;
    --gold:#b97d3e;
    --gold-light:#c99456;
    --indigo:#1e1464;
    --indigo-light:#2e2482;
    --ink:#4a4a4a;
    --ink-dark:#2b2b2b;
  }
  *{margin:0;padding:0;box-sizing:border-box}
  html,body{width:1200px;height:1200px;overflow:hidden;background:var(--bg)}
  .sheet{position:absolute;background:var(--paper);box-shadow:0 4px 14px rgba(0,0,0,.18);overflow:hidden}
  .sheet svg.shapes{position:absolute;inset:0;width:100%;height:100%}

  .letterhead{left:119px;top:278px;width:556px;height:715px}
  .envelope-front{left:714px;top:492px;width:433px;height:216px}
  .envelope-back{left:717px;top:743px;width:429px;height:213px}

  .brand{position:absolute;display:flex;align-items:center;gap:8px}
  .brand-mark{width:26px;height:26px;background:var(--indigo)}
  .brand-name{font-family:"Montserrat",sans-serif;font-weight:700;color:var(--indigo);font-size:17px;letter-spacing:.5px;white-space:nowrap}
  .letterhead .brand{left:60px;top:48px}
  .envelope-front .brand{left:47px;top:32px}
  .envelope-front .brand-mark{width:22px;height:22px}
  .envelope-front .brand-name{font-size:15px}

  .contact{position:absolute;left:381px;top:18px;border-left:1px solid #777;padding-left:10px;font-family:"Open Sans",Arial,sans-serif;font-size:10px;line-height:12px;color:#222}
  .contact li{list-style:none;display:flex;align-items:center;gap:4px}
  .contact svg{width:8px;height:8px;fill:none;stroke:var(--indigo);stroke-width:1.4}

  .letter-block{position:absolute;left:52px;width:450px;font-family:"Lato",sans-serif;font-size:9px;color:var(--ink)}
  .issue-date{top:134px}
  .recipient{top:155px;line-height:11px}
  .salutation{top:216px}
  .body-copy{top:244px}
  .body-copy p{line-height:16px;text-align:justify;margin-bottom:16px}
  .sign-off{top:486px}
  .signature{width:128px;height:15px;margin:10px 0 8px;background:linear-gradient(90deg,#d8d8dc,#eeeef0)}
  .signer{font-size:11.5px;color:var(--ink-dark);margin-bottom:5px}

  .footer-address{position:absolute;left:0;right:0;bottom:10px;text-align:center;font-family:"Lato",sans-serif;font-size:11px;color:#fff}
  .envelope-front .footer-address{left:30px;right:auto;bottom:7px;font-size:7.5px;text-align:left}
</style>
</head>
<body>

<section class="sheet letterhead">
  <svg class="shapes" viewBox="0 0 556 715" preserveAspectRatio="none">
    <defs>
      <linearGradient id="goldFill" x1="0" y1="0" x2="1" y2="1">
        <stop offset="0" stop-color="var(--gold-light)"/><stop offset="1" stop-color="var(--gold)"/>
      </linearGradient>
      <linearGradient id="indigoFill" x1="0" y1="0" x2="1" y2="1">
        <stop offset="0" stop-color="var(--indigo)"/><stop offset="1" stop-color="var(--indigo-light)"/>
      </linearGradient>
    </defs>
    <path d="M0 0 H450 C215 5 32 32 0 144 Z" fill="url(#goldFill)"/>
    <path d="M0 715 V686 H240 C432 686 544 656 556 572 V715 Z" fill="url(#indigoFill)"/>
  </svg>

  <div class="brand"><span class="brand-mark"></span><span class="brand-name">FERN &amp; GABLE REALTY</span></div>

  <ul class="contact">
    <li><svg viewBox="0 0 10 10"><path d="M2 1 L4 3 L3 4 Q4 6 6 7 L7 6 L9 8 L8 9 Q3 9 1 2 Z"/></svg>055-987 654 321</li>
    <li><svg viewBox="0 0 10 10"><rect x="2.5" y="1" width="5" height="8" rx="1"/></svg>055-987 654 321</li>
    <li><svg viewBox="0 0 10 10"><rect x="1" y="2.5" width="8" height="5"/><path d="M1 2.5 L5 6 L9 2.5"/></svg>hello@ferngable.com</li>
    <li><svg viewBox="0 0 10 10"><circle cx="5" cy="5" r="4"/><path d="M1 5 H9 M5 1 Q2 5 5 9 Q8 5 5 1"/></svg>www.ferngable.com</li>
  </ul>

  <p class="letter-block issue-date">Issuing Date: May 5, 2018</p>
  <p class="letter-block recipient">Name Of Employee Mr. XYZABC<br>Address of Employee<br>Address Line 2 etc..</p>
  <p class="letter-block salutation">Dear Mr.XYZABC</p>
  <div class="letter-block body-copy">
    <p>Lorem Ipsum has been the industry's standard dummy text ever since the 1500s, when an unknown printer took a galley of type and scrambled it to make a type specimen book. It has survived not only five centuries, but also the leap into electronic typesetting, remaining essentially unchanged. It was popularised in the 1960s with the release of transfer sheets containing Lorem Ipsum passages, and more recently with desktop publishing software like page layout programs including versions of Lorem Ipsum.</p>
    <p>Lorem Ipsum is simply dummy text of the printing and typesetting industry. Lorem Ipsum has been the industry's standard dummy text ever since the 1500s, when an unknown printer took a galley of type and scrambled it to make a type specimen book.</p>
    <p>It has survived not only five centuries, but also the leap into electronic typesetting, remaining essentially unchanged. It was popularised in the 1960s with the release of transfer sheets containing Lorem IpsumIpsum passages.</p>
  </div>
  <div class="letter-block sign-off">
    <p>Yours Sincerely</p>
    <div class="signature" role="img" aria-label="Handwritten signature of Marcus Ellery"></div>
    <p class="signer">Marcus Ellery</p>
    <p>Managing Director</p>
  </div>

  <p class="footer-address">421, Address line here, dummy code 45452 Country Name</p>
</section>

<section class="sheet envelope-front">
  <svg class="shapes" viewBox="0 0 541 270" preserveAspectRatio="none">
    <defs>
      <linearGradient id="goldFillEnv" x1="0" y1="0" x2="1" y2="1">
        <stop offset="0" stop-color="var(--gold-light)"/><stop offset="1" stop-color="var(--gold)"/>
      </linearGradient>
      <linearGradient id="indigoFillEnv" x1="0" y1="0" x2="1" y2="1">
        <stop offset="0" stop-color="var(--indigo)"/><stop offset="1" stop-color="var(--indigo-light)"/>
      </linearGradient>
    </defs>
    <path d="M0 0 H380 C150 2 20 30 0 125 Z" fill="url(#goldFillEnv)"/>
    <path d="M0 270 V248 H380 C490 248 535 200 541 125 V270 Z" fill="url(#indigoFillEnv)"/>
  </svg>
  <div class="brand"><span class="brand-mark"></span><span class="brand-name">FERN &amp; GABLE REALTY</span></div>
  <p class="footer-address">421, Address line goes here Country Name, 45452</p>
</section>

<section class="sheet envelope-back">
  <svg class="shapes" viewBox="0 0 536 266" preserveAspectRatio="none">
    <defs>
      <linearGradient id="indigoFlap" x1="0" y1="0" x2="1" y2="1">
        <stop offset="0" stop-color="var(--indigo)"/><stop offset="1" stop-color="var(--indigo-light)"/>
      </linearGradient>
    </defs>
    <path d="M0 0 H536 L514 79 H24 Z" fill="url(#indigoFlap)"/>
  </svg>
</section>

</body>
</html>
```